Crystal Clear Ice Ball Maker for whiskey, cocktails

Thank you for taking the time to look at my Product package design project. The product needing packaging designs is a high-end crystal clear ice sphere maker for whiskey, cocktails and drinks. I am hoping to get designs which really make it stand out over competitors with a creative, classy, minimalistic look which shows that it is high end as well as working it in with my logo style and a style which is relevant to an ice maker. The things I would like on the packaging are:

1. My logo
2. Some of the pictures of my product which are provided (use on my project where you feel they will fit)
3. My barcode on the bottom of the box (along with “made in china” for legal requirements)
4. The instructions on the back (or if its better will put them on a separate insert in the box to keep the packaging more minimalistic)

These are my thoughts so far although I am encouraging to share ideas, as I do want the packaging to be world class. Attached is the the logo, barcode and some images from my photoshoot

Target Market(s)

High end professionals, Unisex,

Font styles to use
Serif

Colors

Designer to choose colors to be used in the design.

Requirements
Must have
• open to ideas

```html
<!DOCTYPE html>
<html lang="en">
<head>
<meta charset="utf-8">
<title>Crystal-Clear Ice Ball Maker – Packaging</title>
<link href="https://fonts.googleapis.com/css2?family=Open+Sans:wght@400;600&family=Dancing+Script&display=swap" rel="stylesheet">
<style>
  :root {
    --page: #f4f4f4;
    --panel: #efefef;
    --panel-light: #f6f6f6;
    --slate: #5b5c5f;
    --ink: #2a2a2a;
    --brand: #2f7fa0;
    --frame: #7a7b7e;
    --white: #ffffff;
  }
  * { box-sizing: border-box; margin: 0; padding: 0; }
  html, body { width: 1200px; height: 656px; overflow: hidden; background: var(--page); }
  body { font-family: "Open Sans", Arial, sans-serif; color: var(--ink); }

  .dieline { position: absolute; top: 130px; left: 150px; display: flex; height: 390px; box-shadow: 0 10px 30px rgba(0,0,0,.12); }

  /* Front */
  .front { position: relative; width: 340px; background: var(--panel); }
  .brand { position: absolute; top: 38px; left: 18px; display: flex; align-items: center; gap: 6px; }
  .brand-mark { width: 14px; height: 14px; border: 1.5px solid var(--brand); }
  .brand-name { font-size: 13px; letter-spacing: .5px; color: var(--brand); font-weight: 400; }
  .title { position: absolute; top: 70px; left: 72px; font-weight: 400; line-height: 1.1; white-space: nowrap; }
  .title-line1 { display: block; font-size: 22px; margin-left: 34px; }
  .title-line2 { display: block; font-size: 33px; }
  .front-photo { position: absolute; left: 48px; top: 172px; width: 262px; height: 150px; border-radius: 6px;
    background: linear-gradient(120deg, #3a3b3d 0%, #55575a 55%, #c9a25a 85%, #e9e9e9 100%); }
  .front-band { position: absolute; left: 0; right: 0; bottom: 0; height: 58px; background: var(--slate);
    display: flex; align-items: center; justify-content: center; color: var(--white); font-size: 13px; letter-spacing: .8px; }

  /* Spines */
  .spine { position: relative; width: 110px; background: var(--slate); }
  .spine-title { position: absolute; left: 50%; top: 50%; transform: translate(-50%,-50%) rotate(-90deg);
    white-space: nowrap; color: var(--white); text-align: center; line-height: 1.1; letter-spacing: 2px; }
  .spine-title .small { display: block; font-size: 22px; color: #e6e6e6; }
  .spine-title .large { display: block; font-size: 32px; }

  /* Back */
  .back { position: relative; width: 340px; background: var(--panel-light); }
  .guide { position: absolute; top: 26px; left: 50px; width: 200px; height: 312px; border: 4px solid var(--frame);
    padding: 10px 12px; font-size: 6.5px; line-height: 1.35; }
  .guide h2 { font-size: 12px; font-weight: 400; text-align: center; margin-bottom: 8px; }
  .guide h3 { font-size: 9px; font-weight: 400; text-align: center; margin-bottom: 8px; }
  .guide .intro { text-align: center; margin-bottom: 10px; }
  .guide ol { padding-left: 10px; }
  .guide li { margin-bottom: 7px; }
  .guide .signoff { font-family: "Dancing Script", cursive; font-size: 12px; text-align: center; margin-top: 4px; }
  .marks { position: absolute; left: 200px; bottom: 22px; display: flex; gap: 5px; }
  .marks span { width: 12px; height: 12px; background: #444; border-radius: 2px; }

  /* Right spine */
  .spine-tile { position: absolute; top: 30px; left: 14px; width: 82px; height: 74px; background: var(--panel);
    display: flex; flex-direction: column; align-items: center; justify-content: center; gap: 6px; }
  .spine-tile .brand-name { font-size: 10px; }
  .spine-photo { position: absolute; left: 20px; width: 70px; height: 100px; border-radius: 50%; }
  .spine-photo.glass { top: 140px; background: radial-gradient(circle at 50% 55%, #f1e1a8 0%, #e0e0e0 60%, #bdbdbd 100%); }
  .spine-photo.warm { top: 262px; background: radial-gradient(circle at 50% 55%, #e8a04c 0%, #a5602a 60%, #5a3a22 100%); }
</style>
</head>
<body>
  <div class="dieline">
    <section class="front">
      <div class="brand"><span class="brand-mark"></span><span class="brand-name">NORTHFROST</span></div>
      <h1 class="title">
        <span class="title-line1">Crystal-Clear</span>
        <span class="title-line2">Ice Ball Maker</span>
      </h1>
      <div class="front-photo" role="img" aria-label="Product photo: insulated ice box, silicone sphere mold and a glass of whiskey with a clear ice ball"></div>
      <div class="front-band">SLOW MELTING ICE SHAPES</div>
    </section>

    <section class="spine">
      <div class="spine-title"><span class="small">Crystal-Clear</span><span class="large">Ice Ball Maker</span></div>
    </section>

    <section class="back">
      <div class="guide">
        <h2>Crystal-Clear Ice Ball Maker</h2>
        <h3>QUICK START GUIDE</h3>
        <p class="intro">Wash all parts soap and warm water before first use (except the foam outer box)</p>
        <ol>
          <li>With plastic insert inside foam box, fill with warm to hot water to the bottom of the inner fill line (about 2 from top)</li>
          <li>Assemble silicone mold and slowly lower all the way into the insert filled with water. Water should overflow into the area above the fill holes - top of if necessary</li>
          <li>Place upright in freezer for 24 hours<br>NOTE Time may vary based on specific freezer conditions but do not exceed 30 hours of freezing</li>
          <li>Remove from freezer and peel out mold by pulling on both of the handles on one of ends.</li>
          <li>Separate the two mold halves and serve ice or store for later</li>
        </ol>
        <p class="signoff">Enjoi</p>
      </div>
      <div class="marks"><span></span><span></span><span></span></div>
    </section>

    <section class="spine">
      <div class="spine-tile"><span class="brand-mark"></span><span class="brand-name">NORTHFROST</span></div>
      <div class="spine-photo glass" role="img" aria-label="Photo: clear ice sphere in a glass of whiskey"></div>
      <div class="spine-photo warm" role="img" aria-label="Photo: ice sphere in a warmly lit glass"></div>
    </section>
  </div>
</body>
</html>
```